Velmint website

A clean uncluttered design that shows at glance that we are in the Media and design and publishing business.

We would like to see designs that use colours that show warmth and quality.

The website should show:
- products
- projects

These should be displaxed in spaces that we can add or interchanges with new products or projects.
Updates

Target Market(s)

Business and project managers and buyers and authors.

Industry/Entity Type

Business

Requirements
Must have
• Good colours. Not too strong, not weak, but reflecting quality.

```html
<!DOCTYPE html>
<html lang="en">
<head>
<meta charset="utf-8">
<title>Velmint</title>
<link href="https://fonts.googleapis.com/css2?family=Arimo:wght@400;700&display=swap" rel="stylesheet">
<style>
  :root {
    --sand: #f4dfb1;
    --sand-light: #f7ead0;
    --frame: #f6e6c2;
    --orange: #ee7a1e;
    --orange-band: #f29a2e;
    --orange-active: #f5a647;
    --green: #5e9a80;
    --green-dark: #4f8a72;
    --green-button: #6aae92;
    --green-text: #4c9a78;
    --taupe: #a08a60;
    --taupe-text: #ae9a74;
    --footer-text: #e3efe6;
    --white: #ffffff;
  }
  * { margin: 0; padding: 0; box-sizing: border-box; }
  html, body { width: 1200px; height: 1145px; overflow: hidden; }
  body { font-family: "Arimo", Arial, sans-serif; background: var(--sand); position: relative; }
  h1, h2, h3 { font-weight: 400; }
  a { text-decoration: none; }
  .abs { position: absolute; }

  /* Header */
  .brand { left: 24px; top: 20px; display: flex; align-items: center; gap: 12px; }
  .brand-mark { width: 50px; height: 50px; background: var(--green); }
  .brand-name { font-size: 54px; font-weight: 700; color: var(--orange); letter-spacing: 1px; line-height: 1; }
  .search { left: 849px; top: 28px; width: 287px; height: 39px; background: var(--sand-light); border: 1px solid #ead3a0;
    font-size: 13px; color: #8a7550; padding: 12px 14px; }
  .search-button { left: 1136px; top: 28px; width: 46px; height: 39px; background: var(--orange); }

  /* Navigation */
  .main-nav { left: 615px; top: 97px; height: 46px; display: flex; background: var(--orange); }
  .main-nav a { color: var(--white); font-size: 19px; padding: 13px 17px 0; text-transform: uppercase; letter-spacing: -0.3px; }
  .main-nav a.active { background: var(--orange-active); }

  /* Hero */
  .hero-band { left: 0; top: 143px; width: 1200px; height: 342px; background: var(--orange-band); }
  .hero-frame { left: 20px; top: 97px; width: 567px; height: 356px; background: var(--frame); }
  .hero-photo { left: 31px; top: 108px; width: 546px; height: 335px; background: linear-gradient(135deg, #d9d4cc 0%, #7b6e66 45%, #3b302c 100%); }
  .hero-title { left: 622px; top: 186px; font-size: 39px; line-height: 46px; color: var(--white); letter-spacing: -0.3px; white-space: nowrap; }
  .hero-text { left: 622px; top: 243px; width: 552px; font-size: 16px; line-height: 20.4px; color: var(--white); }
  .read-more { left: 618px; top: 367px; width: 156px; height: 44px; display: flex; background: var(--green-button); color: var(--white); font-size: 17px; }
  .read-more .tab { width: 31px; background: var(--green-dark); display: flex; align-items: center; justify-content: center; }
  .read-more .label { padding: 12px 0 0 16px; }

  /* Featured projects */
  .section-title { left: 16px; top: 510px; font-size: 41px; line-height: 48px; color: var(--green); letter-spacing: -0.5px; }
  .project { top: 580px; width: 158px; }
  .project-image { width: 158px; height: 158px; }
  .project-text { margin-top: 12px; font-size: 14.4px; line-height: 17.8px; color: var(--green-text); }
  .project-link { margin-top: 13px; width: 22px; height: 21px; background: var(--green); display: flex; align-items: center; justify-content: center; }
  .divider { top: 580px; width: 1px; height: 297px; background: #e2c994; }

  /* Why choose us */
  .why-panel { left: 806px; top: 485px; width: 377px; height: 426px; background: var(--sand-light); }
  .why-title { left: 829px; top: 526px; font-size: 32px; line-height: 38px; color: var(--taupe); }
  .why-text { left: 831px; top: 579px; width: 335px; font-size: 16px; line-height: 20.5px; color: var(--taupe-text); }
  .why-text p + p { margin-top: 20.5px; }

  /* Footer */
  .footer { left: 0; top: 911px; width: 1200px; height: 234px; background: var(--green); }
  .footer-heading { top: 937px; font-size: 21px; line-height: 24px; color: var(--white); }
  .footer-list { top: 979px; list-style: none; font-size: 14.4px; line-height: 17.8px; color: var(--footer-text); }
  .quote-icon { left: 505px; top: 980px; }
  .quote-text { left: 576px; top: 981px; width: 270px; font-size: 14.4px; line-height: 17.8px; color: var(--footer-text); }
  .quote-author { left: 571px; top: 1041px; font-size: 17px; color: var(--white); }
  .quote-author span { color: var(--footer-text); font-size: 14px; }
  .social { left: 922px; top: 981px; display: flex; gap: 10px; }
  .social span { width: 34px; height: 34px; border-radius: 50%; background: #c9ddd0; }
  .newsletter-note { left: 922px; top: 1025px; font-size: 13.2px; line-height: 16px; color: var(--footer-text); }
  .email-field { left: 920px; top: 1067px; width: 166px; height: 33px; background: var(--white); font-size: 13px; color: var(--green-dark); padding: 9px 12px; }
  .subscribe { left: 1086px; top: 1067px; width: 86px; height: 33px; background: var(--orange); color: var(--white); font-size: 14px; padding: 9px 0 0 14px; }
</style>
</head>
<body>

<header>
  <div class="abs brand"><span class="brand-mark"></span><span class="brand-name">Velmint</span></div>
  <div class="abs search">search ...</div>
  <div class="abs search-button">
    <svg width="46" height="39" viewBox="0 0 46 39"><circle cx="20" cy="16" r="7" fill="none" stroke="#fff" stroke-width="3"/><line x1="25" y1="21" x2="33" y2="29" stroke="#fff" stroke-width="4" stroke-linecap="round"/></svg>
  </div>
</header>

<div class="abs hero-band"></div>

<nav class="abs main-nav">
  <a class="active" href="#">Home</a><a href="#">About</a><a href="#">Products</a><a href="#">Projects</a><a href="#">Contact</a>
</nav>

<section class="hero">
  <div class="abs hero-frame"></div>
  <div class="abs hero-photo" role="img" aria-label="Photo of two colleagues reviewing printed layouts at a desk"></div>
  <h1 class="abs hero-title">Lorem ipsum dolor sit amet elit</h1>
  <p class="abs hero-text">Ut wisi enim ad minim veniam, quis nostrud exerci tation ullamcorper suscipit lobortis nisl ut aliquip ex ea commodo consequat. Duis autem vel eum iriure dolor in hendrerit in vulputate velit esse molestie consequat, vel illum dolore eu feugiat nulla facilisis at vero eros et accumsan et iusto odio dignissim qui blandit.</p>
  <a class="abs read-more" href="#"><span class="tab"><svg width="8" height="8" viewBox="0 0 8 8"><path d="M1 0 L7 4 L1 8Z" fill="#cfe6da"/></svg></span><span class="label">Read more</span></a>
</section>

<section class="featured">
  <h2 class="abs section-title">Featured Projects</h2>

  <article class="abs project" style="left:16px">
    <div class="project-image" role="img" aria-label="Corporate stationery set with colourful flower motif" style="background:linear-gradient(135deg,#e9eef2,#8fa6b4 60%,#4d5a62)"></div>
    <p class="project-text">Lorem ipsum dolor sit amet, consectetuer adipiscing elit, sed diam nonummy nibh euismod tincidunt .</p>
    <div class="project-link"><svg width="8" height="8" viewBox="0 0 8 8"><path d="M1 0 L7 4 L1 8Z" fill="#e3efe6"/></svg></div>
  </article>
  <div class="abs divider" style="left:195px"></div>

  <article class="abs project" style="left:217px">
    <div class="project-image" role="img" aria-label="Brochure mockups in green and purple" style="background:linear-gradient(135deg,#ffffff,#e6e3e8 50%,#a66aa8)"></div>
    <p class="project-text">Lorem ipsum dolor sit amet, consectetuer adipiscing elit, sed diam nonummy nibh euismod tincidunt .</p>
    <div class="project-link"><svg width="8" height="8" viewBox="0 0 8 8"><path d="M1 0 L7 4 L1 8Z" fill="#e3efe6"/></svg></div>
  </article>
  <div class="abs divider" style="left:394px"></div>

  <article class="abs project" style="left:416px">
    <div class="project-image" role="img" aria-label="Book cover with gear artwork on dark background" style="background:linear-gradient(160deg,#3a3a3a,#1c1c1c 55%,#6b6b6b)"></div>
    <p class="project-text">Lorem ipsum dolor sit amet, consectetuer adipiscing elit, sed diam nonummy nibh euismod tincidunt .</p>
    <div class="project-link"><svg width="8" height="8" viewBox="0 0 8 8"><path d="M1 0 L7 4 L1 8Z" fill="#e3efe6"/></svg></div>
  </article>
  <div class="abs divider" style="left:595px"></div>

  <article class="abs project" style="left:617px">
    <div class="project-image" role="img" aria-label="Brochure design in teal and orange" style="background:linear-gradient(135deg,#f3efe4,#9cc9c9 55%,#e7b06a)"></div>
    <p class="project-text">Lorem ipsum dolor sit amet, consectetuer adipiscing elit, sed diam nonummy nibh euismod tincidunt .</p>
    <div class="project-link"><svg width="8" height="8" viewBox="0 0 8 8"><path d="M1 0 L7 4 L1 8Z" fill="#e3efe6"/></svg></div>
  </article>
</section>

<aside>
  <div class="abs why-panel"></div>
  <h2 class="abs why-title">Why Choose Us?</h2>
  <div class="abs why-text">
    <p>Consectetuer adipiscing elit, sed diam nonummy nibh euismod tincidunt ut laoreet dolore magna aliquam erat volutpat. Ut wisi enim ad minim veniam, quis nostrud exerci tation ullamcorper suscipit lobortis nisl ut aliquip ex ea commodo consequat.</p>
    <p>Duis autem vel eum iriure dolor in hendrerit in vulputate velit esse molestie consequat, vel illum dolore eu feugiat nulla facilisis at vero eros et accumsan et iusto odio dignissim qui blandit praesent luptatum zzril delenit augue duis dolore te feugait nulla facilisi.</p>
  </div>
</aside>

<footer>
  <div class="abs footer"></div>

  <h3 class="abs footer-heading" style="left:26px">Navigation</h3>
  <ul class="abs footer-list" style="left:26px"><li>Home</li><li>About</li><li>Products</li><li>Projects</li><li>Contact Us</li></ul>

  <h3 class="abs footer-heading" style="left:238px">Products</h3>
  <ul class="abs footer-list" style="left:238px"><li>Media</li><li>Design</li><li>Publishing</li><li>Book Cover</li><li>Calling Cards</li></ul>
  <ul class="abs footer-list" style="left:371px"><li>Brochure</li><li>Books</li><li>CD Cover</li><li>Branding</li></ul>

  <h3 class="abs footer-heading" style="left:505px">Testimonial</h3>
  <svg class="abs quote-icon" width="56" height="52" viewBox="0 0 56 52">
    <path d="M4 4 H34 V26 H14 L6 34 V26 H4Z" fill="none" stroke="#d7e7dc" stroke-width="3" stroke-linejoin="round"/>
    <path d="M22 20 H52 V42 H50 V50 L42 42 H22Z" fill="#d7e7dc"/>
  </svg>
  <p class="abs quote-text">At vero eos et accusamus et iusto odio dignissimos ducimus, qui blanditiis praesentium voluptatum deleniti atque.</p>
  <p class="abs quote-author"><span>- </span>Dana Whitlow</p>

  <h3 class="abs footer-heading" style="left:918px">Connect with Us</h3>
  <div class="abs social"><span></span><span></span><span></span><span></span><span></span></div>
  <p class="abs newsletter-note">subscribe to our monthly newsletter<br>and get the best deals and discounts</p>
  <div class="abs email-field">enter email</div>
  <div class="abs subscribe">subscribe</div>
</footer>

</body>
</html>
```